Income Tax Flyer - Updates Needed

Just need to update this flyer design and give it a new look. We would like to keep all the same wording but make it stand out a little more. Our selling point is the "Same Day Tax Advance up to $6,000"

Industry/Entity Type

Lending, Small Loans, Tax Services, Title Loans, Personal Loans

```html
<!DOCTYPE html>
<html lang="en">
<head>
<meta charset="UTF-8">
<title>Easy Advance Tax Flyer</title>
<link href="https://fonts.googleapis.com/css2?family=Poppins:wght@300;600;700&family=Roboto+Condensed:wght@700&display=swap" rel="stylesheet">
<style>
:root{
  --stage:#d2d3d5;
  --green:#0d5632;
  --green-deep:#083f24;
  --green-light:#2a7a4f;
  --red:#c21f26;
  --white:#ffffff;
  --suit:#14161f;
}
*{margin:0;padding:0;box-sizing:border-box}
html,body{width:1119px;height:1200px;overflow:hidden;background:var(--stage)}
body{position:relative;font-family:'Poppins',sans-serif}
.flyer{position:absolute;left:304px;top:245px;width:514px;height:726px;overflow:hidden;background:var(--green)}
.banknote-backdrop{position:absolute;inset:0;background:linear-gradient(135deg,var(--green-deep) 0%,var(--green) 35%,var(--green-light) 62%,var(--green) 80%,var(--green-deep) 100%)}
.presenter-photo{position:absolute;left:0;top:104px;width:244px;height:510px;background:linear-gradient(180deg,#6d5448 0%,#2a2c38 22%,var(--suit) 60%,#0e1017 100%);border-radius:0 60px 0 0}
.brand{position:absolute;left:43px;top:44px;width:110px;text-align:center;color:var(--white);font-weight:600;font-size:17px;line-height:1.1}
.headline{position:absolute;left:243px;top:42px;width:260px;text-align:center;color:var(--white);font-weight:300;font-size:20px;line-height:26px}
.headline-badge{position:absolute;left:257px;top:101px;width:243px;height:34px;background:var(--red);color:var(--white);font-family:'Roboto Condensed',sans-serif;font-weight:700;font-size:28px;line-height:34px;text-align:center}
.offer-card{position:absolute;left:265px;top:207px;width:236px;height:186px;border-radius:14px;background:var(--red);overflow:hidden}
.offer-title{height:45px;background:var(--white);color:var(--green);font-family:'Roboto Condensed',sans-serif;font-weight:700;font-size:23px;line-height:47px;text-align:center;border-radius:14px 14px 0 0}
.offer-amount{color:var(--white);font-weight:700;font-size:49px;text-align:center;line-height:1}
.offer-amount.primary{margin-top:16px}
.offer-amount.max{position:absolute;left:5px;top:114px;width:227px;height:66px;background:var(--green);border-radius:12px;line-height:66px}
.perks{position:absolute;left:299px;top:430px;list-style:none}
.perk{display:flex;align-items:center;height:36px;margin-bottom:30px}
.perk svg{width:36px;height:36px;margin-right:10px;flex:none}
.perk-label{color:var(--white);font-weight:600;font-size:9px;line-height:12px;text-transform:uppercase}
.footer-wave{position:absolute;left:0;top:0;width:514px;height:726px}
.contact{position:absolute;left:27px;top:643px;color:var(--white);font-weight:700;font-size:17px}
</style>
</head>
<body>
<main class="flyer">
  <div class="banknote-backdrop" role="img" aria-label="Green-tinted photo of stacked dollar banknotes"></div>
  <div class="presenter-photo" role="img" aria-label="Photo of a smiling man in a dark suit holding a pointer"></div>

  <div class="brand">Keystone Tax Lending</div>

  <p class="headline">FILE YOUR TAXES<br>AND APPLY FOR AN</p>
  <div class="headline-badge">EASY ADVANCE!</div>

  <section class="offer-card">
    <div class="offer-title">APPLY HERE FOR TODAY!</div>
    <div class="offer-amount primary">$5,000</div>
    <div class="offer-amount max">$6000</div>
  </section>

  <ul class="perks">
    <li class="perk">
      <svg viewBox="0 0 36 36" fill="none" stroke="#fff" stroke-width="1.6" stroke-linecap="round">
        <circle cx="18" cy="20" r="13"/><circle cx="18" cy="20" r="9"/>
        <path d="M15 4h6M18 4v3M29 9l2-2"/>
        <path d="M20.5 16.5c-.6-.8-1.5-1-2.5-1-1.4 0-2.3.7-2.3 1.7 0 2.4 5 1.3 5 3.9 0 1.1-1 1.9-2.7 1.9-1.1 0-2-.4-2.6-1.2M18 14v1.5M18 22.5V24"/>
      </svg>
      <span class="perk-label">Available in<br>24 hours or less</span>
    </li>
    <li class="perk">
      <svg viewBox="0 0 36 36" fill="none" stroke="#fff" stroke-width="1.6" stroke-linecap="round" stroke-linejoin="round">
        <path d="M14 27A12 12 0 1 1 30 15"/>
        <path d="M16 11c-.5-.7-1.2-1-2-1-1.1 0-1.9.6-1.9 1.4 0 2 4 1.1 4 3.2 0 .9-.8 1.6-2.2 1.6-.9 0-1.6-.3-2.1-1M14 8.5V10M14 16.2v1.3"/>
        <path d="M20 33l-4-6c-.6-1 .6-2 1.4-1.2L20 28V16c0-1.6 2.4-1.6 2.4 0v7l6 1.2c1 .2 1.6 1 1.5 2L29 33"/>
      </svg>
      <span class="perk-label">Choose your<br>loan amount</span>
    </li>
    <li class="perk">
      <svg viewBox="0 0 36 36" fill="none" stroke="#fff" stroke-width="1.6" stroke-linecap="round" stroke-linejoin="round">
        <rect x="13" y="3" width="18" height="26" rx="2"/>
        <path d="M24.5 11c-.6-.8-1.4-1.1-2.3-1.1-1.3 0-2.2.7-2.2 1.6 0 2.2 4.6 1.2 4.6 3.6 0 1-.9 1.8-2.5 1.8-1 0-1.9-.4-2.4-1.1M22.2 8v1.8M22.2 16.9v1.6"/>
        <path d="M4 26l6-7c1-1 2.5-.6 2.5.8L12 23l4-3c1-.8 2.4.5 1.5 1.6L11 30l-4 3"/>
      </svg>
      <span class="perk-label">Quick &amp;<br>easy</span>
    </li>
  </ul>

  <svg class="footer-wave" viewBox="0 0 514 726" aria-hidden="true">
    <path d="M0 612C120 600 260 640 367 662C430 673 480 660 514 644V726H0Z" fill="#e9e9ea"/>
    <path d="M0 612C120 600 260 640 367 662C430 673 480 660 514 644" fill="none" stroke="#111" stroke-width="1.5"/>
    <path d="M0 620C120 611 260 652 367 671C430 682 480 669 514 656V726H0Z" fill="var(--red)"/>
  </svg>

  <div class="contact">Contact:</div>
</main>
</body>
</html>
```